Artificial Intelligence based service Veltranoquest.ai

Looking for a website for service designed for driving schools to deliver AI based solutions and features. File are to include various pages from contact to list of services to faqs, demos and more. we are looking for a website for AI based service for driving schools. services will include things like chat bots, voice agent, document processing and ai based marketing.

Target Market(s)

driving school owners and managers.

Industry/Entity Type

software and AI

Number of Pages Required

4 page

Font styles to use
Sans Serif

Requirements
Must have
• clean and easy to navigate pages. responsive. also delivery via FIGMA.

```html
<!DOCTYPE html>
<html lang="en">
<head>
<meta charset="utf-8">
<title>Veltranoquest.ai – 24/7 Voice Agent for Driving Schools</title>
<link rel="stylesheet" href="https://fonts.googleapis.com/css2?family=Montserrat:wght@500;600;700;800;900&family=Open+Sans:wght@400;600;700&display=swap">
<style>
:root{
  --navy:#0b1628;
  --navy-deep:#060e1c;
  --navy-mid:#12264a;
  --glow:#2f7fd8;
  --green:#72bf44;
  --green-dark:#5aa531;
  --ink:#14181f;
  --muted:#4a5260;
  --soft:#eef3eb;
  --white:#ffffff;
}
*{box-sizing:border-box;margin:0;padding:0}
html,body{width:1200px;height:4612px;overflow:hidden}
body{font-family:"Open Sans",Arial,sans-serif;color:var(--ink);background:var(--white);position:relative}
h1,h2,h3,.brand,.btn,.nav a{font-family:"Montserrat",Arial,sans-serif}
.section{position:absolute;left:0;width:1200px}

/* header */
.site-header{top:0;height:100px;background:var(--white);z-index:5}
.brand{position:absolute;left:40px;top:28px;display:flex;align-items:center;gap:12px;font-weight:800;font-size:26px;color:var(--navy)}
.brand-dot{width:34px;height:34px;border-radius:50%;background:var(--green)}
.contact-bar{position:absolute;right:40px;top:14px;display:flex;align-items:center;gap:26px;font-size:13px;color:var(--ink)}
.contact-item{display:flex;align-items:center;gap:8px}
.contact-icon{width:24px;height:24px;border-radius:50%;background:var(--navy);display:flex;align-items:center;justify-content:center}
.btn{display:inline-flex;align-items:center;justify-content:center;border-radius:20px;font-weight:700;font-size:11px;letter-spacing:.5px;text-transform:uppercase;padding:0 20px;height:34px;white-space:nowrap}
.btn-green{background:var(--green);color:var(--white)}
.btn-outline{border:2px solid var(--ink);color:var(--ink);background:transparent}
.btn-white{background:var(--white);color:var(--navy)}
.nav{position:absolute;left:516px;top:66px;display:flex;gap:30px}
.nav a{font-size:11px;font-weight:700;color:var(--ink);text-decoration:none;letter-spacing:.3px;padding-bottom:6px}
.nav a.active{color:var(--green);border-bottom:2px solid var(--green)}

/* hero */
.hero{top:100px;height:860px;background:var(--navy-deep);overflow:hidden}
.hero-visual{position:absolute;right:0;top:0;width:760px;height:860px;background:radial-gradient(ellipse at 62% 40%,#3a8fe6 0%,#1a4d93 28%,#0d2347 55%,var(--navy-deep) 80%)}
.hero-copy{position:absolute;left:128px;top:88px;width:520px}
.hero-title{font-size:46px;line-height:52px;font-weight:900;color:var(--white);letter-spacing:1px}
.accent{color:var(--green)}
.hero-sub{margin-top:22px;font-size:17px;line-height:25px;color:var(--green);font-weight:600}
.hero-copy .btn{margin-top:26px}
.hero-arrows{position:absolute;left:128px;top:540px;display:flex;gap:22px}
.wave{position:absolute;left:0;width:1200px}

/* why */
.why{top:960px;height:420px}
.why-frame{position:absolute;left:178px;top:0;width:478px;height:330px;border:3px solid var(--green);border-radius:28px}
.why-visual{position:absolute;left:140px;top:22px;width:498px;height:318px;border-radius:22px;background:linear-gradient(135deg,#0b1f44 0%,#1b4f9c 45%,#3a86de 60%,#0f2650 100%)}
.why-copy{position:absolute;left:700px;top:50px;width:400px}
.section-title{font-size:34px;line-height:38px;font-weight:900;color:var(--ink)}
.dashes{display:flex;gap:6px;margin:14px 0 18px}
.dashes span{width:16px;height:5px;border-radius:3px;background:var(--green)}
.center .dashes{justify-content:center}
.why-copy p{font-size:13px;line-height:21px;color:var(--muted)}
.why-copy .btn{margin-top:22px;height:32px}

/* problems */
.problems{top:1420px;height:920px;background:var(--soft)}
.problems-head{position:absolute;left:0;top:80px;width:1200px;text-align:center}
.cards{position:absolute;left:140px;top:200px;width:920px;display:grid;grid-template-columns:repeat(3,300px);gap:40px 10px}
.card{background:var(--white);border-radius:8px;height:300px;padding:28px 26px;box-shadow:0 6px 20px rgba(20,40,20,.08)}
.card-icon{width:58px;height:58px;border-radius:50%;background:var(--green);display:flex;align-items:center;justify-content:center;margin-bottom:18px}
.card h3{font-size:14px;line-height:19px;font-weight:800;color:var(--ink);margin-bottom:10px}
.card p{font-size:12px;line-height:18px;color:var(--muted)}
.card p.result{margin-top:10px}
.result b{color:var(--green-dark)}

/* benefits */
.benefits{top:2340px;height:580px}
.benefits-copy{position:absolute;left:140px;top:120px;width:460px}
.benefit-list{list-style:none;margin-top:6px}
.benefit-list li{display:flex;align-items:center;gap:12px;font-size:14px;line-height:20px;margin-bottom:11px;color:var(--ink)}
.tick{width:18px;height:18px;flex:none}
.benefits-visual{position:absolute;left:640px;top:60px;width:480px;height:420px;border-radius:220px 0 0 220px;background:radial-gradient(circle at 55% 50%,#3d93ea 0%,#1c5aa8 35%,#0d2a57 70%,#0a1a36 100%)}

/* cta */
.cta{top:2920px;height:660px;background:var(--navy-deep);overflow:hidden}
.cta-copy{position:absolute;left:0;top:200px;width:1200px;text-align:center}
.cta-title{font-size:46px;line-height:54px;font-weight:900;color:var(--white)}
.cta-sub{margin-top:26px;font-size:16px;color:var(--white)}
.cta-actions{margin-top:26px;display:flex;justify-content:center;gap:16px}

/* testimonial */
.testimonial{top:3580px;height:400px;text-align:center}
.testimonial .brand{position:static;justify-content:center;margin-top:30px;font-size:30px}
.quote{margin:36px auto 0;width:820px;font-family:"Montserrat",Arial,sans-serif;font-size:26px;line-height:34px;font-weight:800;color:var(--navy)}
.cite{margin-top:18px;font-size:16px;color:var(--muted)}

/* footer */
.site-footer{top:3980px;height:632px;background:var(--navy-deep);overflow:hidden;text-align:center}
.site-footer .brand{position:absolute;left:0;top:380px;width:1200px;justify-content:center;color:var(--white);font-size:34px}
.copyright{position:absolute;left:0;top:520px;width:1200px;font-size:13px;color:#c6cfdc}
</style>
</head>
<body>

<header class="section site-header">
  <div class="brand"><span class="brand-dot"></span>Veltranoquest.ai</div>
  <div class="contact-bar">
    <div class="contact-item">
      <span class="contact-icon"><svg width="12" height="12" viewBox="0 0 24 24"><path fill="#fff" d="M6.6 10.8a15 15 0 0 0 6.6 6.6l2.2-2.2c.3-.3.7-.4 1-.2 1.1.4 2.3.6 3.6.6.6 0 1 .4 1 1V20c0 .6-.4 1-1 1A17 17 0 0 1 3 4c0-.6.4-1 1-1h3.5c.6 0 1 .4 1 1 0 1.3.2 2.5.6 3.6.1.3 0 .7-.2 1z"/></svg></span>
      Call : +1 555-0142-7788
    </div>
    <div class="contact-item">
      <span class="contact-icon"><svg width="12" height="12" viewBox="0 0 24 24"><path fill="#fff" d="M3 5h18v14H3zm2 2v.5l7 4.5 7-4.5V7l-7 4.5z"/></svg></span>
      info@veltranoquest.ai
    </div>
    <span class="btn btn-green">Book a Free Demo</span>
  </div>
  <nav class="nav">
    <a class="active">HOME</a>
    <a>KEY PROBLEMS SOLVED</a>
    <a>REAL BENEFITS FOR YOUR SCHOOL</a>
    <a>BLOG</a>
    <a>CONTACT US</a>
  </nav>
</header>

<section class="section hero">
  <div class="hero-visual" role="img" aria-label="Woman wearing a headset in profile, surrounded by glowing blue AI light effects"></div>
  <div class="hero-copy">
    <h1 class="hero-title">BOOST YOUR<br><span class="accent">DRIVING</span> SCHOOL<br>WITH A <span class="accent">24/7</span><br>VOICE AGENT</h1>
    <p class="hero-sub">Automate Calls. Answer Questions Instantly.<br>Never Miss a Student Again.</p>
    <span class="btn btn-green">Talk to a Product Specialist</span>
  </div>
  <div class="hero-arrows">
    <svg width="28" height="16" viewBox="0 0 28 16"><path d="M27 8H3M9 2 3 8l6 6" stroke="#fff" stroke-width="2.5" fill="none"/></svg>
    <svg width="28" height="16" viewBox="0 0 28 16"><path d="M1 8h24M19 2l6 6-6 6" stroke="#fff" stroke-width="2.5" fill="none"/></svg>
  </div>
  <svg class="wave" style="top:700px" height="160" viewBox="0 0 1200 160" preserveAspectRatio="none">
    <path d="M0 80 C300 150 600 150 900 80 C1020 52 1120 40 1200 44 L1200 160 L0 160Z" fill="#ffffff"/>
    <path d="M0 62 C300 132 600 132 900 62 C1020 34 1120 22 1200 26" stroke="var(--green)" stroke-width="3" fill="none"/>
  </svg>
</section>

<section class="section why">
  <div class="why-frame"></div>
  <div class="why-visual" role="img" aria-label="Hands typing on a laptop with a glowing AI chatbot hologram above the keyboard"></div>
  <div class="why-copy">
    <h2 class="section-title">WHY DRIVING<br>SCHOOLS CHOOSE<br>VOICE AGENTS</h2>
    <div class="dashes"><span></span><span></span><span></span></div>
    <p>Running a driving school means juggling lesson schedules, student questions, staff changes, and constant phone calls. A Voice Agent is your AI-powered assistant that answers the phone 24/7, handles routine questions, and gives your staff room to breathe—without the cost of hiring more people.</p>
    <span class="btn btn-outline">Learn More</span>
  </div>
</section>

<section class="section problems">
  <div class="problems-head center">
    <h2 class="section-title">KEY PROBLEMS SOLVED</h2>
    <div class="dashes"><span></span><span></span><span></span></div>
  </div>
  <div class="cards">
    <article class="card">
      <div class="card-icon"><svg width="28" height="28" viewBox="0 0 24 24"><path fill="#fff" d="M6.6 10.8a15 15 0 0 0 6.6 6.6l2.2-2.2c.3-.3.7-.4 1-.2 1.1.4 2.3.6 3.6.6.6 0 1 .4 1 1V20c0 .6-.4 1-1 1A17 17 0 0 1 3 4c0-.6.4-1 1-1h3.5c.6 0 1 .4 1 1 0 1.3.2 2.5.6 3.6.1.3 0 .7-.2 1z"/></svg></div>
      <h3>HIGH CALL VOLUME &amp;<br>REPETITIVE QUESTIONS</h3>
      <p>Let your voice agent handle calls about Pricing, Permit requirements, Class availability, Road test slots</p>
      <p class="result"><b>Result:</b> Less time answering the same questions, more time delivering great lessons.</p>
    </article>
    <article class="card">
      <div class="card-icon"><svg width="28" height="28" viewBox="0 0 24 24"><circle cx="12" cy="12" r="9" stroke="#fff" stroke-width="2" fill="none"/><path d="M12 7v5l3 3" stroke="#fff" stroke-width="2" fill="none"/></svg></div>
      <h3>AFTER-HOURS<br>AVAILABILITY</h3>
      <p>Missed calls = missed business. Your voice agent works evenings, weekends, and holidays.</p>
      <p class="result"><b>Result:</b> Convert more inquiries into paying students—even while you sleep.</p>
    </article>
    <article class="card">
      <div class="card-icon"><svg width="28" height="28" viewBox="0 0 24 24"><circle cx="12" cy="8" r="4" fill="#fff"/><path d="M4 21c0-4.4 3.6-7 8-7s8 2.6 8 7z" fill="#fff"/></svg></div>
      <h3>ADMIN STAFF<br>TURNOVER</h3>
      <p>Hiring and training office staff takes time. A voice agent is ready on day one.</p>
      <p class="result"><b>Result:</b> Consistent, professional service no matter who's at the front desk.</p>
    </article>
    <article class="card">
      <div class="card-icon"><svg width="28" height="28" viewBox="0 0 24 24"><rect x="3" y="5" width="18" height="16" rx="2" stroke="#fff" stroke-width="2" fill="none"/><path d="M3 10h18M8 3v4M16 3v4" stroke="#fff" stroke-width="2"/></svg></div>
      <h3>INSTRUCTOR ABSENCES<br>&amp; RESCHEDULING</h3>
      <p>Integrates with your booking system, your voice agent can help reschedule or notify students of changes.</p>
      <p class="result"><b>Result:</b> Fewer cancellations and smoother communication.</p>
    </article>
    <article class="card">
      <div class="card-icon"><svg width="28" height="28" viewBox="0 0 24 24"><path d="M7 18h10a4 4 0 0 0 .5-8A6 6 0 0 0 6 9a4.5 4.5 0 0 0 1 9z" fill="#fff"/></svg></div>
      <h3>NO EXPENSIVE TECH<br>INVESTMENT</h3>
      <p>Voice agents run in the cloud and integrate with your existing phone system.</p>
      <p class="result"><b>Result:</b> No hardware, low setup costs, and immediate ROI.</p>
    </article>
    <article class="card">
      <div class="card-icon"><svg width="28" height="28" viewBox="0 0 24 24"><circle cx="12" cy="12" r="9" stroke="#fff" stroke-width="2" fill="none"/><path d="M3 12h18M12 3c3 3 3 15 0 18M12 3c-3 3-3 15 0 18" stroke="#fff" stroke-width="1.6" fill="none"/></svg></div>
      <h3>LANGUAGE<br>BARRIERS</h3>
      <p>Serve more students with support for multiple languages.</p>
      <p class="result"><b>Result:</b> Improve access and satisfaction for non-English-speaking families.</p>
    </article>
  </div>
</section>

<section class="section benefits">
  <div class="benefits-copy">
    <h2 class="section-title">REAL BENEFITS<br>FOR YOUR SCHOOL</h2>
    <div class="dashes"><span></span><span></span><span></span></div>
    <ul class="benefit-list">
      <li><svg class="tick" viewBox="0 0 18 18"><circle cx="9" cy="9" r="9" fill="var(--green)"/><path d="M5 9.2l2.7 2.6L13 6.4" stroke="#fff" stroke-width="2" fill="none"/></svg>24/7 live call support—no more missed calls</li>
      <li><svg class="tick" viewBox="0 0 18 18"><circle cx="9" cy="9" r="9" fill="var(--green)"/><path d="M5 9.2l2.7 2.6L13 6.4" stroke="#fff" stroke-width="2" fill="none"/></svg>Faster response times = happier customers</li>
      <li><svg class="tick" viewBox="0 0 18 18"><circle cx="9" cy="9" r="9" fill="var(--green)"/><path d="M5 9.2l2.7 2.6L13 6.4" stroke="#fff" stroke-width="2" fill="none"/></svg>Less admin stress for you and your team</li>
      <li><svg class="tick" viewBox="0 0 18 18"><circle cx="9" cy="9" r="9" fill="var(--green)"/><path d="M5 9.2l2.7 2.6L13 6.4" stroke="#fff" stroke-width="2" fill="none"/></svg>Lower operating costs than live staff</li>
      <li><svg class="tick" viewBox="0 0 18 18"><circle cx="9" cy="9" r="9" fill="var(--green)"/><path d="M5 9.2l2.7 2.6L13 6.4" stroke="#fff" stroke-width="2" fill="none"/></svg>More bookings, fewer no-shows</li>
      <li><svg class="tick" viewBox="0 0 18 18"><circle cx="9" cy="9" r="9" fill="var(--green)"/><path d="M5 9.2l2.7 2.6L13 6.4" stroke="#fff" stroke-width="2" fill="none"/></svg>A modern, professional image</li>
    </ul>
  </div>
  <div class="benefits-visual" role="img" aria-label="Glowing blue digital network of connected data panels"></div>
</section>

<section class="section cta">
  <svg class="wave" style="top:0" height="170" viewBox="0 0 1200 170" preserveAspectRatio="none">
    <path d="M0 0 L1200 0 L1200 60 C900 150 500 150 0 70Z" fill="#ffffff"/>
    <path d="M0 90 C500 170 900 170 1200 80" stroke="var(--green)" stroke-width="3" fill="none"/>
  </svg>
  <div class="cta-copy">
    <h2 class="cta-title">READY TO AUTOMATE<br>YOUR FRONT DESK?</h2>
    <p class="cta-sub">Let your school sound smarter, faster, and more helpful—24 hours a day</p>
    <div class="cta-actions">
      <span class="btn btn-green">Talk to a Product Specialist</span>
      <span class="btn btn-white">Book a Free Demo</span>
      <span class="btn btn-green">See It in Action</span>
    </div>
  </div>
  <svg class="wave" style="top:540px" height="120" viewBox="0 0 1200 120" preserveAspectRatio="none">
    <path d="M0 40 C400 110 800 110 1200 30 L1200 120 L0 120Z" fill="#ffffff"/>
    <path d="M0 24 C400 94 800 94 1200 14" stroke="var(--green)" stroke-width="3" fill="none"/>
  </svg>
</section>

<section class="section testimonial">
  <div class="brand"><span class="brand-dot"></span>Veltranoquest.ai</div>
  <p class="quote">“SINCE ADDING A VOICE AGENT, WE'VE CUT OUR CALL VOLUME IN HALF—AND ENROLLMENT IS UP!”</p>
  <p class="cite">— Dana Whitfield, Director, BrightLane Driving School</p>
</section>

<footer class="section site-footer">
  <svg class="wave" style="top:0" height="200" viewBox="0 0 1200 200" preserveAspectRatio="none">
    <path d="M0 0 L1200 0 L1200 70 C800 170 400 170 0 80Z" fill="#ffffff"/>
    <path d="M0 110 C400 200 800 200 1200 100" stroke="var(--green)" stroke-width="3" fill="none"/>
  </svg>
  <div class="brand"><span class="brand-dot"></span>Veltranoquest.ai</div>
  <p class="copyright">Driving schools © 2025. All Rights Reserved.</p>
</footer>

</body>
</html>
```